integrative health clinic-Medical massage, acupuncture, chiropractic

we like our logo, but are open to new ideas. We need a new card design. We have added chiropractic and acupuncture that we have put under the name of the business. We are an integrative medical clinic

Target Market(s)

General public, athletes

Contact Information for Business Card

Phone 5055583927
Fax 5055583926
Hours Monday-Friday 9-6
Saturday 10-6
The 20% can be smaller on the back

Colors
3176b5
0355a3

Requirements
Must have
• Logo but am open to ideas
Nice to have
• We are an integrated medical clinic but also want to be personable. We want the card fun and inviting

```html
<!DOCTYPE html>
<html lang="en">
<head>
<meta charset="utf-8">
<title>Vital Frame Wellness – Business Card</title>
<link href="https://fonts.googleapis.com/css2?family=Roboto:ital,wght@0,300;0,400;0,500;1,300&family=Crimson+Text:ital@1&display=swap" rel="stylesheet">
<style>
  :root {
    --stage: #1d1d1f;
    --ink: #0a0a0a;
    --blue: #0355a3;
    --blue-light: #3176b5;
    --white: #ffffff;
    --text-dark: #111111;
  }
  * { margin: 0; padding: 0; box-sizing: border-box; }
  html, body {
    width: 1200px; height: 900px; overflow: hidden;
    background: var(--stage);
    font-family: "Roboto", Arial, sans-serif;
  }
  .stage {
    width: 1200px; height: 900px;
    display: flex; flex-direction: column; align-items: center; justify-content: center;
    gap: 36px;
  }
  .card { position: relative; width: 700px; height: 400px; overflow: hidden; }

  /* Back side */
  .card--back { background: var(--ink); color: var(--white); }
  .brand {
    position: absolute; top: 34px; left: 0; right: 0;
    display: flex; align-items: center; justify-content: center; gap: 22px;
  }
  .brand__dot { width: 54px; height: 54px; border-radius: 50%; background: var(--blue-light); }
  .brand__name { font-size: 44px; font-weight: 500; line-height: 1; color: var(--white); }
  .brand__tagline {
    font-family: "Crimson Text", Georgia, serif; font-style: italic;
    font-size: 21px; margin-top: 4px; letter-spacing: .3px;
  }
  .brand__services {
    font-size: 14px; letter-spacing: 1.2px; text-transform: uppercase;
    color: var(--blue-light); margin-top: 4px;
  }
  .offer-band {
    position: absolute; top: 168px; left: 0; right: 0; height: 36px;
    background: var(--blue);
    display: flex; align-items: center; justify-content: center;
    font-size: 16px; letter-spacing: .5px;
  }
  .book-online { position: absolute; top: 226px; left: 0; right: 0; text-align: center; font-size: 19px; }
  .label { color: var(--blue-light); }
  .hours { position: absolute; top: 282px; left: 0; right: 0; text-align: center; font-size: 19px; }
  .hours .divider { color: var(--blue-light); margin: 0 12px; }
  .insurance { position: absolute; top: 314px; left: 0; right: 0; text-align: center; font-size: 16px; }
  .social-dot {
    position: absolute; right: 28px; bottom: 26px;
    width: 26px; height: 26px; border-radius: 50%; background: var(--blue-light);
  }

  /* Front side */
  .card--front { background: var(--white); }
  .card__waves { position: absolute; inset: 0; }
  .front-brand {
    position: absolute; top: 36px; left: 48px;
    display: flex; align-items: center; gap: 16px;
  }
  .front-brand__dot { width: 88px; height: 88px; border-radius: 50%; background: var(--blue); flex: none; }
  .front-brand__name { font-size: 28px; font-weight: 500; color: var(--blue); line-height: 1.15; }
  .front-brand__services {
    font-size: 13px; letter-spacing: 1px; text-transform: uppercase;
    color: var(--blue-light); margin-top: 6px; white-space: nowrap;
  }
  .specialty {
    position: absolute; top: 130px; right: 38px; text-align: right;
    font-size: 19px; line-height: 1.2; color: var(--text-dark);
  }
  .contact {
    position: absolute; right: 22px; top: 252px;
    list-style: none; color: var(--white); text-align: right; font-size: 17px;
  }
  .contact li { display: flex; align-items: center; justify-content: flex-end; gap: 10px; height: 24px; }
  .contact .address { line-height: 1.15; height: auto; margin-bottom: 4px; padding-right: 30px; }
  .contact svg { width: 20px; height: 20px; flex: none; }
</style>
</head>
<body>
<main class="stage">

  <section class="card card--back" aria-label="Card back">
    <div class="brand">
      <span class="brand__dot"></span>
      <div>
        <div class="brand__name">Vital Frame Wellness</div>
        <div class="brand__tagline">Sports Therapy and Wellness Center</div>
        <div class="brand__services">Medical Massage · Acupuncture · Chiropractic</div>
      </div>
    </div>
    <div class="offer-band">20% OFF FIRST VISIT</div>
    <p class="book-online"><span class="label">BOOK ONLINE:</span> www.vitalframewellnessnm.com</p>
    <p class="hours"><span class="label">HOURS:</span> Monday-Friday 9am-6pm<span class="divider">|</span>Saturday 10am-6pm</p>
    <p class="insurance">We accept some insurances, Worker's Comp and Personal Injury</p>
    <span class="social-dot"></span>
  </section>

  <section class="card card--front" aria-label="Card front">
    <svg class="card__waves" viewBox="0 0 700 400" preserveAspectRatio="none">
      <path fill="#0a0a0a" d="M0,168 C130,232 330,232 500,200 C600,182 680,198 700,212 L700,236 C660,218 570,206 480,214 C330,236 140,244 0,196 Z"/>
      <path fill="#0355a3" d="M0,218 C160,272 360,246 520,232 C610,225 680,240 700,252 L700,400 L0,400 Z"/>
    </svg>
    <div class="front-brand">
      <span class="front-brand__dot"></span>
      <div>
        <div class="front-brand__name">Vital Frame<br>Wellness</div>
        <div class="front-brand__services">Medical Massage · Acupuncture · Chiropractic</div>
      </div>
    </div>
    <p class="specialty">Specializing in Medical, Sports<br>Massage and Manual Therapies</p>
    <ul class="contact">
      <li class="address">1847 Cordova Ln, B4. Santa Fe<br>NM 87508</li>
      <li>505 558 3927
        <svg viewBox="0 0 24 24" fill="none" stroke="#fff" stroke-width="1.8"><circle cx="12" cy="12" r="10"/><path d="M8.5 7.5l2 2-1.2 1.4a7 7 0 0 0 3.8 3.8l1.4-1.2 2 2-1.5 1.5c-3.5-.3-7.7-4.5-8-8z"/></svg></li>
      <li>505 558 3926
        <svg viewBox="0 0 24 24" fill="#fff"><rect x="7" y="3" width="10" height="6"/><rect x="3" y="10" width="18" height="8" rx="1.5"/><rect x="7" y="15" width="10" height="6" stroke="#0355a3" stroke-width="1.2"/></svg></li>
      <li>info@vitalframewellnessnm.com
        <svg viewBox="0 0 24 24" fill="none" stroke="#fff" stroke-width="1.8"><rect x="3" y="6" width="18" height="12"/><path d="M3 6l9 7 9-7"/></svg></li>
      <li>www.vitalframewellnessnm.com
        <svg viewBox="0 0 24 24" fill="none" stroke="#fff" stroke-width="1.6"><circle cx="12" cy="12" r="9"/><ellipse cx="12" cy="12" rx="4" ry="9"/><path d="M3 12h18M5 7h14M5 17h14"/></svg></li>
    </ul>
  </section>

</main>
</body>
</html>
```